Book Cover Design 'Boundless Tide - Lessons In Inner Sovereignty'

I need to see pitches / artwork for a book cover for new book designed to start a new global spiritual movement and save humanity. The book merges science and spirituality and explains to the reader why they are an all powerful god.

```html
<!DOCTYPE html>
<html lang="en">
<head>
<meta charset="utf-8">
<title>Boundless Tide – Lessons In Inner Sovereignty</title>
<link rel="stylesheet" href="https://fonts.googleapis.com/css2?family=Anton&family=Poppins:wght@800;900&family=Montserrat:wght@400&display=swap">
<style>
  :root {
    --page-bg: #d9d9d9;
    --cover-white: #ffffff;
    --ink: #0b0b0b;
    --band: #050505;
    --band-text: #f2f2f2;
    --glow-pink: #e9bdee;
    --glow-lilac: #d3cdf2;
    --glow-soft: #f7f0fb;
    --gold-soft: #f2c84a;
    --gold-deep: #d99a16;
  }
  * { margin: 0; padding: 0; box-sizing: border-box; }
  html, body {
    width: 1200px;
    height: 1092px;
    overflow: hidden;
    background: var(--page-bg);
  }
  .cover {
    position: absolute;
    left: 250px;
    top: 26px;
    width: 700px;
    height: 1040px;
    background: var(--cover-white);
    overflow: hidden;
    box-shadow: 0 10px 30px rgba(0,0,0,0.18);
  }
  .cover__glow {
    position: absolute;
    left: -60px;
    top: 240px;
    width: 880px;
    height: 700px;
    background: radial-gradient(ellipse 50% 50% at 55% 50%,
      var(--glow-soft) 0%,
      var(--glow-pink) 40%,
      var(--glow-lilac) 68%,
      rgba(255,255,255,0) 100%);
  }
  .cover__title {
    position: absolute;
    left: 40px;
    top: 34px;
    font-family: "Anton", sans-serif;
    font-size: 158px;
    font-weight: 400;
    line-height: 0.98;
    color: var(--ink);
    text-transform: uppercase;
    letter-spacing: -1px;
  }
  .cover__illustration {
    position: absolute;
    left: 258px;
    top: 450px;
    width: 250px;
    height: 220px;
    background: linear-gradient(180deg, var(--gold-soft), var(--gold-deep));
  }
  .cover__subtitle {
    position: absolute;
    left: 40px;
    right: 40px;
    top: 735px;
    font-family: "Poppins", sans-serif;
    color: var(--ink);
    text-transform: uppercase;
    text-align: right;
  }
  .cover__subtitle-lead {
    display: block;
    font-weight: 800;
    font-size: 38px;
    line-height: 1.1;
    letter-spacing: -0.5px;
  }
  .cover__subtitle-main {
    display: block;
    font-weight: 900;
    font-size: 66px;
    line-height: 1.05;
    letter-spacing: -1.5px;
  }
  .cover__band {
    position: absolute;
    left: 0;
    bottom: 0;
    width: 100%;
    height: 118px;
    background: var(--band);
    display: flex;
    align-items: center;
    justify-content: center;
  }
  .cover__author {
    font-family: "Montserrat", sans-serif;
    font-weight: 400;
    font-size: 30px;
    letter-spacing: 16px;
    color: var(--band-text);
    text-transform: uppercase;
    padding-left: 16px;
  }
</style>
</head>
<body>
  <main class="cover">
    <div class="cover__glow" role="img" aria-label="Soft pink and lilac radiant mandala background"></div>
    <h1 class="cover__title">Boundless<br>Tide</h1>
    <div class="cover__illustration" role="img" aria-label="Glossy golden sculpture illustration"></div>
    <h2 class="cover__subtitle">
      <span class="cover__subtitle-lead">Lessons in inner</span>
      <span class="cover__subtitle-main">Sovereignty</span>
    </h2>
    <footer class="cover__band">
      <p class="cover__author">Marten Holloway</p>
    </footer>
  </main>
</body>
</html>
```